Redo of existing website www.stonvira.example

I would like it to look like the newer style website, with large images, less text. clean and modern looking. The new design should focus on call to action. ultimately that's what were looking for.Some features I would like to see we try to do good job of keeping up with our blog, and it is a good source of recent pictures of our work. I like four visitors to get the few pieces they're doing with a national brand or franchise pray. I like to stay far from the idea of a local one-man band with magnetic signs on his truck.
I think that clean beautiful images have the biggest impact. In my opinion most people don't read more than a couple lines of text. The text is more for search engines.
we are currently in the process of revising our logo as well, I will upload those files when I get them.
Please feel free to use content and images from our current website www.stonvira.example. we can purchase professional stock images if needed.
1. large call to action with easy contact form.
2. Blog roll on front page to showcase our recent work.
2. All social connect buttons.
Check out our reviews on ratewell!
My current websites
Www.stonvira.example
https://social.example/profile/604918273655102938417/about
www.socialpage.example/stonvira
http://www.blogsite.example/blog/curbguardian
https://microblog.example/Stonvira
websites I like the way they look.
http://quillpost.example/
http://www.cartwell.example/
http://www.brennickpaving.example/
http://www.tarmacways.example/
http://curbandcoatingworks.example/
Hello all,
I have just uploaded some images of our company mascot "Curb Guardian" and our new logo.
Project Deadline Extended
Reason: Death in family. Finally back to work.
Target Market(s)
We have 2 main groups of customers commercial and residential.
Commercial customers are Property owners and managers, operators of multi location business, restaurant, supermarket, banks, and are best source for repeat business
for Residential customers we provide driveway repair and driveway paving services.
for residential customers I would like to encourge the submission or pictures with the inquiry for a quick quote. Residential customers are typically a one time job but are a good source of referrals
I like how this website separates residential and commercial
http://www.glintcoatonline.example
Call

```html
<!DOCTYPE html>
<html lang="en">
<head>
<meta charset="utf-8">
<title>Stonvira — Asphalt Paving</title>
<link href="https://fonts.googleapis.com/css2?family=Open+Sans:wght@400;600;700;800&display=swap" rel="stylesheet">
<style>
:root{
  --green:#19c21e;
  --green-dark:#0e9a13;
  --red:#d8262a;
  --ink:#222;
  --text:#555;
  --page:#3a3b3c;
  --page-dark:#2a2b2c;
  --panel:#ffffff;
  --soft:#f1f1f1;
  --grey-head:#5a5a5a;
}
*{box-sizing:border-box;margin:0;padding:0}
html,body{width:802px;height:1200px;overflow:hidden}
body{font-family:"Open Sans",Arial,sans-serif;background:var(--page);color:var(--text);position:relative}
.site{position:absolute;left:60px;top:0;width:682px;height:1200px;background:var(--panel)}
.header{height:80px;display:flex;align-items:center;justify-content:space-between;padding:0 22px}
.brand{display:flex;align-items:center;gap:10px}
.brand-mark{width:22px;height:22px;background:var(--green)}
.brand-name{font-weight:600;font-size:26px;color:var(--ink);line-height:1}
.phone{background:var(--red);color:#fff;font-weight:700;font-size:14px;padding:5px 12px 5px 10px;border-radius:4px;display:flex;align-items:center;gap:8px}
.nav{height:20px;background:var(--green);display:flex;padding-left:14px}
.nav a{color:#fff;font-size:10px;font-weight:600;text-decoration:none;padding:0 14px;line-height:20px;border-right:1px solid rgba(255,255,255,.4)}
.nav a:first-child{background:var(--green-dark)}
.hero{height:250px;background:linear-gradient(180deg,#9fc3e6 0%,#c7d9ea 40%,#8c8f92 62%,#4b4d50 100%);position:relative}
.dots{position:absolute;bottom:8px;left:50%;transform:translateX(-50%);display:flex;gap:5px}
.dots i{width:7px;height:7px;background:#fff;opacity:.6;display:block}
.dots i:first-child{opacity:1}
.services{height:280px;background:linear-gradient(180deg,#3b3c3d 0 90px,var(--soft) 90px);display:flex;justify-content:center;gap:46px;padding-top:20px}
.service{width:246px;height:240px;background:#fff;border:1px solid #ddd;box-shadow:0 2px 6px rgba(0,0,0,.2);text-align:center;padding-top:14px}
.service-icon{width:62px;height:62px;border-radius:50%;background:var(--green);margin:0 auto;display:flex;align-items:center;justify-content:center}
.service h2{font-size:24px;font-weight:400;color:var(--ink);margin:10px 0 6px;line-height:30px}
.service p{font-size:9px;line-height:13px;padding:0 26px}
.btn-more{display:inline-block;background:#444;color:#fff;font-size:9px;padding:5px 18px;margin-top:10px;border-radius:2px}
.columns{display:flex;gap:14px;padding:18px 22px 0;height:205px}
.col{flex:1}
.col h3{background:var(--grey-head);color:#fff;font-weight:400;font-size:15px;padding:3px 8px}
.col ul{list-style:none;font-size:10px;line-height:15px;margin-top:6px;color:var(--ink)}
.col li::before{content:"";display:inline-block;width:6px;height:6px;background:var(--green);margin-right:6px}
.post{font-size:10px;color:var(--ink);margin-top:7px;line-height:13px}
.post small{display:block;color:var(--green-dark);font-size:8px}
.quote{font-size:10px;line-height:14px;margin-top:6px}
.author{color:var(--red);font-size:11px;text-align:right;margin-top:6px}
.view{font-size:8px;text-align:right;margin-top:6px;color:var(--ink)}
.featured{padding:0 22px;height:195px}
.featured h3{color:var(--green);font-weight:400;font-size:20px;margin-bottom:10px}
.projects{display:flex;gap:12px}
.project{flex:1;text-align:center;font-size:10px;color:var(--ink)}
.project .ph{height:100px;margin-bottom:8px}
.p1{background:linear-gradient(#9ab3c6,#3a3a3a)}
.p2{background:linear-gradient(#b8c3cc,#2f3133)}
.p3{background:linear-gradient(#6d8fc4,#303236)}
.p4{background:linear-gradient(#c5c9c2,#5b5e5a)}
.cta-band{height:120px;background:var(--page-dark);display:flex;align-items:center;justify-content:space-between;padding:0 20px}
.video{width:170px;height:96px;background:linear-gradient(#6f8496,#1e1e1e);position:relative}
.video-bar{position:absolute;bottom:0;left:0;right:0;height:12px;background:#000}
.quote-btn{width:124px;height:78px;background:#4d5257;border:2px solid #6a6f74;color:#d9dde0;font-weight:800;font-size:20px;text-align:center;line-height:30px;padding-top:8px}
.newsletter{width:190px;color:#fff}
.newsletter h4{font-weight:400;font-size:14px;line-height:15px;display:flex;gap:8px;align-items:center}
.newsletter input{width:100%;height:16px;margin-top:8px;font-size:8px;padding:0 4px;border:0}
.newsletter .go{display:inline-block;background:var(--green);font-size:8px;padding:2px 10px;margin-top:5px}
.footer{height:50px;text-align:center;font-size:8px;color:#ccc;background:var(--page-dark);padding-top:10px;line-height:12px}
</style>
</head>
<body>
<div class="site">
  <header class="header">
    <div class="brand">
      <span class="brand-mark"></span>
      <span class="brand-name">Stonvira</span>
    </div>
    <div class="phone">
      <svg width="13" height="13" viewBox="0 0 24 24"><path fill="#fff" d="M6.6 10.8a15 15 0 0 0 6.6 6.6l2.2-2.2c.3-.3.7-.4 1-.2 1.1.4 2.3.6 3.6.6.6 0 1 .4 1 1V20c0 .6-.4 1-1 1A17 17 0 0 1 3 4c0-.6.4-1 1-1h3.5c.6 0 1 .4 1 1 0 1.3.2 2.5.6 3.6.1.3 0 .7-.2 1z"/></svg>
      (555) 014-2739
    </div>
  </header>
  <nav class="nav">
    <a href="#">Home</a><a href="#">Commercial</a><a href="#">Residential</a><a href="#">About Us</a><a href="#">Free Estimate</a><a href="#">Testimonials</a><a href="#">Blog</a>
  </nav>
  <section class="hero" role="img" aria-label="Paving truck sealing a shopping plaza parking lot under a blue sky">
    <div class="dots"><i></i><i></i><i></i></div>
  </section>
  <section class="services">
    <div class="service">
      <div class="service-icon">
        <svg width="34" height="30" viewBox="0 0 36 32"><rect x="2" y="14" width="32" height="16" fill="#fff"/><rect x="6" y="4" width="24" height="10" fill="#fff"/><rect x="10" y="18" width="6" height="12" fill="#19c21e"/><rect x="20" y="18" width="10" height="6" fill="#19c21e"/></svg>
      </div>
      <h2>Commercial</h2>
      <p>From routine asphalt maintenance and parking lot repairs to major projects, such as new parking lot overlays, paving for resurfacing and complete commercial reconstruction.</p>
      <span class="btn-more">Learn more →</span>
    </div>
    <div class="service">
      <div class="service-icon">
        <svg width="34" height="30" viewBox="0 0 36 32"><path d="M18 2 2 16h5v14h22V16h5z" fill="#fff"/><rect x="15" y="20" width="6" height="10" fill="#19c21e"/></svg>
      </div>
      <h2>Residential</h2>
      <p>Favored for its ability to create a sturdy, seamless blacktop driveway patch in areas that do not have serious structural or sub-grade asphalt deterioration, this method saves.</p>
      <span class="btn-more">Learn more →</span>
    </div>
  </section>
  <section class="columns">
    <div class="col">
      <h3>What we do..</h3>
      <ul>
        <li>Paving &amp; Resurfacing</li><li>Patching &amp; Repairs</li><li>Crack Filling</li><li>Sealcoating</li><li>Striping &amp; Lot Marking</li><li>Lot Maintenance Plans</li><li>Complete year-round care</li><li>with easy monthly payments</li><li>Clients &amp; References</li>
      </ul>
    </div>
    <div class="col">
      <h3>Blog</h3>
      <div class="post">Trip hazards? We're on it!<small>April 2013</small></div>
      <div class="post">When should you sealcoat your asphalt pavement?<small>April 2013</small></div>
      <div class="post">If 60: How big is this Dozer?<small>April 2013</small></div>
      <div class="view">View all</div>
    </div>
    <div class="col">
      <h3>What people say!</h3>
      <p class="quote">Lorem ipsum, from gravida nibh elit sed auctor aliquet. Aenean sollicitudin, lorem quis bibendum auctor, nisi elit consequat ipsum, nec sagittis sem nibh id elit. Duis sed odio sit amet nibh vulputate cursus a sit amet mauris. Morbi accumsan ipsum velit.</p>
      <div class="author">Marta J. Lindqvist</div>
      <div class="view">View all</div>
    </div>
  </section>
  <section class="featured">
    <h3>Featured projects</h3>
    <div class="projects">
      <div class="project"><div class="ph p1" role="img" aria-label="Crew resurfacing a road"></div>Lorem ipsum pesn</div>
      <div class="project"><div class="ph p2" role="img" aria-label="Freshly sealed parking lot"></div>Lorem ipsum pesn</div>
      <div class="project"><div class="ph p3" role="img" aria-label="Painted accessible parking marking"></div>Lorem ipsum pesn</div>
      <div class="project"><div class="ph p4" role="img" aria-label="Repaved residential driveway"></div>Lorem ipsum pesn</div>
    </div>
  </section>
  <section class="cta-band">
    <div class="video" role="img" aria-label="Company video showing paving work"><div class="video-bar"></div></div>
    <div class="quote-btn">GET FREE<br>QUOTE</div>
    <div class="newsletter">
      <h4><svg width="26" height="20" viewBox="0 0 26 20"><rect x="1" y="1" width="24" height="18" fill="none" stroke="#fff" stroke-width="2"/><path d="M1 1l12 10L25 1" fill="none" stroke="#fff" stroke-width="2"/></svg>Sign up<br>Newsletter</h4>
      <input type="text" placeholder="Your Email Address">
      <span class="go">Subscribe</span>
    </div>
  </section>
  <footer class="footer">
    Privacy Policy &nbsp;|&nbsp; Site Map &nbsp;|&nbsp; Syracuse NY &nbsp;|&nbsp; Buffalo NY &nbsp;|&nbsp; Rochester NY &nbsp;|&nbsp; Cleveland OH<br>
    © 2013 Stonvira Inc. All Rights Reserved
  </footer>
</div>
</body>
</html>
```